Quillbrook, Collaboration Ecosystem for the Integration of Logistics Services

We need a website to build Quillbrook logistics orchestration services, across America. The moonshot Quillbrook invites to integrate under a "logistics button" the entire supply chains of physical goods, to people, in cities (just as financial services do with their payment button in e-commerce) . Quillbrook is a commitment to the unimaginable, to obtain a stratospheric success, the company will be integrated with the academy and local governments, in the construction of: Common standards for the integration of services; Technologically validate the services; Develop product traceability technologies in exchanges between companies; Give regulatory and legal compliance in the automated delivery of products; and make payments within the supply chain with each delivery of products to a person.
The pandemic has challenged us as a species, it has shown us that human collaboration is essential to give our species sustainability. Today we cannot act alone and we need more collaboration mechanisms to satisfy our needs. Quillbrook is a journey into the unknown, an area of development outside the traditional models of logistics services in cities, everything has changed and will change again.
Quillbrook is a B2B business. Solves the delivery of products in an urban territory, integrates under a decentralized technological model of services to the different actors involved in the supply chains of each of the goods that people consume from their homes. For users, the Quillbrook delivery button implies the contracting of a service according to their requirements: The exact date and time of delivery, the value of caring for the environment, the technology involved in delivery, the importance of people and their well-being in the supply chain.
It is important that the design reflects technology, collaboration and sales explosion. We attach our logo.
Important points are: we are incorporating the companies through a membership to initially finance the project; we will have a launch event in November 2022; and we will carry out content and advertising campaigns to generate visibility for this initiative, which is revolutionary. Short-term objectives of the project are: to publicize the project through social networks and online to incorporate partner companies, publicize the November launch event and show the progress in the integration process of companies in the "logistics button Quillbrook. Finally, we would like the design to be adapted for the Wix platform.

Target Market(s)

Primary target: Big companies in the transportation and logistics services. Secondary target: Big companies in the rest of the economy.

Coding

Coded - Design and coding required

Number of Pages Required

5+ page

Font styles to use
Serif

Requirements
Must have
• Home to explain the project in one image
Spectacular Big Banner
Countdown with the project deadline: 365 days to launch the Quillbrook logistics button
Landing page for seminar inscriptions
Landing page for membership sales
Visually communicate high tech, collaboration and sales Big Bang for the companies that will participate
Once we have the initial group of companies, we need a a template to communicate the missions (as if we are going to the Moon or Mars) that the companies will commit. For instance, The Technology is a mission; International Funding is another mission; Integration is another mission, and so forth.
Nice to have
• Websites we love:

https://redvale.skorvant.org/

https://plendaroute.com/

https://www.tunquaworks.com/
Should not have
• Boring images, colors or whatever...

```html
<!DOCTYPE html>
<html lang="en">
<head>
<meta charset="utf-8">
<title>Quillbrook — Ecosystem for the Integration of Logistics</title>
<link rel="stylesheet" href="https://fonts.googleapis.com/css2?family=Poppins:wght@100;200;400;500;600;700;800&display=swap">
<style>
  :root {
    --white: #ffffff;
    --ink: #0b0b10;
    --brand-blue: #4a5cf0;
    --brand-violet: #5c5ff2;
    --dial-grey: #c7ccd8;
    --panel-dark: rgba(18, 16, 20, 0.78);
    --footer-navy: #1a2344;
    --hero-top: #4a4650;
    --hero-bottom: #9a5a30;
    --count-top: #7f97ae;
    --count-bottom: #5d6a5a;
    --mission-top: #3f5088;
    --mission-bottom: #5d5f7e;
  }
  * { box-sizing: border-box; margin: 0; padding: 0; }
  html, body { width: 1200px; height: 2295px; overflow: hidden; }
  body { font-family: "Poppins", sans-serif; color: var(--white); position: relative; background: var(--footer-navy); }

  .section { position: absolute; left: 0; width: 1200px; overflow: hidden; }

  /* Brand */
  .brand { position: absolute; display: flex; align-items: center; gap: 14px; }
  .brand-dot { width: 62px; height: 62px; border-radius: 50%; background: var(--brand-blue); }
  .brand-name { font-weight: 800; font-size: 27px; letter-spacing: 1.5px; color: var(--white); }

  /* Hero */
  .hero { top: 0; height: 605px; }
  .hero-photo { position: absolute; inset: 0; background: linear-gradient(180deg, var(--hero-top) 0%, var(--hero-bottom) 100%); }
  .nav { position: absolute; top: 52px; left: 0; width: 1200px; font-size: 12.5px; font-weight: 500; }
  .nav a { position: absolute; color: var(--white); text-decoration: none; white-space: nowrap; }
  .cta-logistics { position: absolute; left: 1022px; top: 44px; width: 101px; height: 35px; border-radius: 18px;
    background: var(--white); color: var(--brand-blue); font-size: 12px; font-weight: 500;
    display: flex; align-items: center; justify-content: center; text-decoration: none; }
  .hero-panel { position: absolute; left: 686px; top: 219px; width: 437px; height: 251px;
    background: var(--panel-dark); border-right: 2px solid var(--brand-blue); }
  .hero-title { position: absolute; left: 704px; top: 248px; font-size: 49px; font-weight: 700; line-height: 61px; letter-spacing: -0.3px; }

  /* Countdown */
  .countdown { top: 605px; height: 605px; }
  .countdown-photo { position: absolute; inset: 0; background: linear-gradient(180deg, var(--count-top) 0%, var(--count-bottom) 100%); }
  .rings { position: absolute; left: 0; top: 0; }
  .deadline-disc { position: absolute; left: 333px; top: 37px; width: 534px; height: 534px; border-radius: 50%;
    background: radial-gradient(circle at 50% 50%, #ffffff 0%, #f4f4f6 70%, #f7f7f7 100%); }
  .deadline-title { position: absolute; left: 0; width: 1200px; top: 94px; text-align: center;
    color: var(--ink); font-size: 25px; font-weight: 600; }
  .dial { position: absolute; left: 450px; top: 155px; }
  .days-number { position: absolute; left: 0; width: 1200px; top: 238px; text-align: center;
    color: var(--ink); font-size: 116px; font-weight: 100; line-height: 1; letter-spacing: 2px; }
  .days-label { position: absolute; left: 0; width: 1200px; top: 356px; text-align: center;
    color: var(--ink); font-size: 19px; font-weight: 400; letter-spacing: 3px; }
  .launch-pill { position: absolute; left: 510px; top: 472px; width: 185px; height: 45px; border-radius: 23px;
    background: var(--ink); color: var(--white); font-size: 10px; font-weight: 600; line-height: 13px;
    text-align: center; display: flex; align-items: center; justify-content: center; }

  /* Missions */
  .missions { top: 1210px; height: 605px; }
  .missions-photo { position: absolute; inset: 0; background: linear-gradient(180deg, var(--mission-top) 0%, var(--mission-bottom) 100%); }
  .missions-title { position: absolute; left: 146px; top: 148px; font-size: 50px; font-weight: 700; }
  .missions-sub { position: absolute; left: 149px; top: 225px; font-size: 21px; font-weight: 400; }
  .mission-list { position: absolute; left: 150px; top: 298px; list-style: none; font-size: 15px; }
  .mission-list li { display: flex; align-items: center; height: 26px; }
  .mission-list svg { width: 14px; height: 14px; margin-right: 20px; }

  /* Footer */
  .footer { top: 1815px; height: 480px; }
  .footer-photo { position: absolute; inset: 0; background: var(--footer-navy); }
  .footer .brand { left: 472px; top: 65px; }
  .footer-about { position: absolute; left: 0; width: 1200px; top: 155px; text-align: center; font-size: 13px; line-height: 25px; }
  .subscribe { position: absolute; left: 367px; top: 229px; width: 452px; height: 49px; border-radius: 25px;
    background: var(--white); display: flex; align-items: center; padding: 0 34px 0 36px; justify-content: space-between; }
  .subscribe span { color: #555a66; font-size: 12.5px; }
  .footer-nav { position: absolute; left: 0; top: 307px; width: 1200px; font-size: 12.5px; font-weight: 500; }
  .footer-nav a { position: absolute; color: var(--white); text-decoration: none; white-space: nowrap; }
  .copyright { position: absolute; left: 0; width: 1200px; top: 338px; text-align: center; font-size: 12.5px; font-weight: 500; }
  .social { position: absolute; top: 380px; width: 46px; height: 46px; border-radius: 50%; background: var(--white);
    color: var(--brand-blue); font-size: 9px; font-weight: 600; display: flex; align-items: center; justify-content: center; }
  .social.is-active { background: var(--brand-violet); color: var(--white); }
</style>
</head>
<body>

<section class="section hero">
  <div class="hero-photo" role="img" aria-label="Photo: worker in a hard hat with a tablet beside a highway with trucks at sunset, overlaid with a network of location pins"></div>
  <div class="brand" style="left:62px;top:24px;">
    <span class="brand-dot"></span><span class="brand-name">QUILLBROOK</span>
  </div>
  <nav class="nav">
    <a style="left:380px">Home</a>
    <a style="left:443px">Seminar Inscriptions</a>
    <a style="left:595px">Membership Sales</a>
    <a style="left:732px">News &amp; Events</a>
    <a style="left:846px">Missions</a>
    <a style="left:924px">Contact</a>
  </nav>
  <a class="cta-logistics">LOGISTICS</a>
  <div class="hero-panel"></div>
  <h1 class="hero-title">Ecosystem for<br>the Integration<br>of Logistics</h1>
</section>

<section class="section countdown">
  <div class="countdown-photo" role="img" aria-label="Photo: white truck driving along a mountain highway under a cloudy sky"></div>
  <svg class="rings" width="1200" height="605" viewBox="0 0 1200 605">
    <circle cx="600" cy="304" r="395" fill="none" stroke="rgba(255,255,255,.75)" stroke-width="2"/>
    <circle cx="600" cy="304" r="455" fill="none" stroke="rgba(255,255,255,.3)" stroke-width="10"/>
  </svg>
  <div class="deadline-disc"></div>
  <h2 class="deadline-title">Project Deadline</h2>
  <svg class="dial" width="300" height="300" viewBox="0 0 300 300">
    <defs>
      <linearGradient id="arcGrad" x1="0" y1="0" x2="0" y2="1">
        <stop offset="0" stop-color="#37b8e6"/>
        <stop offset="1" stop-color="#e83fd8"/>
      </linearGradient>
    </defs>
    <circle cx="150" cy="150" r="122" fill="none" stroke="var(--dial-grey)" stroke-width="4"/>
    <path d="M150 28 A122 122 0 0 1 210 256" fill="none" stroke="url(#arcGrad)" stroke-width="3"/>
    <circle cx="210" cy="256" r="3" fill="#e83fd8"/>
    <g stroke="#9aa0ad" stroke-width="1.5">
      <line x1="150" y1="6" x2="150" y2="14"/>
      <line x1="187" y1="11" x2="185" y2="19"/>
      <line x1="222" y1="25" x2="218" y2="32"/>
      <line x1="252" y1="48" x2="246" y2="54"/>
      <line x1="275" y1="78" x2="268" y2="82"/>
      <line x1="289" y1="113" x2="281" y2="115"/>
      <line x1="294" y1="150" x2="286" y2="150"/>
      <line x1="289" y1="187" x2="281" y2="185"/>
      <line x1="275" y1="222" x2="268" y2="218"/>
      <line x1="252" y1="252" x2="246" y2="246"/>
      <line x1="113" y1="11" x2="115" y2="19"/>
    </g>
  </svg>
  <div class="days-number">365</div>
  <div class="days-label">DAYS</div>
  <div class="launch-pill">365 DAYS TO LAUNCH THE<br>QUILLBROOK LOGISTICS</div>
</section>

<section class="section missions">
  <div class="missions-photo" role="img" aria-label="Photo: blue semi-trailer truck on an open highway at sunset"></div>
  <h2 class="missions-title">Our Missions</h2>
  <p class="missions-sub">if we are going to the Moon or Mars</p>
  <ul class="mission-list">
    <li><svg viewBox="0 0 14 14"><path d="M1 7 L5 12 L13 1" fill="none" stroke="#fff" stroke-width="1.6"/></svg>The Technology is a mission</li>
    <li><svg viewBox="0 0 14 14"><path d="M1 7 L5 12 L13 1" fill="none" stroke="#fff" stroke-width="1.6"/></svg>International Funding is another mission</li>
    <li><svg viewBox="0 0 14 14"><path d="M1 7 L5 12 L13 1" fill="none" stroke="#fff" stroke-width="1.6"/></svg>Integration is another mission</li>
    <li><svg viewBox="0 0 14 14"><path d="M1 7 L5 12 L13 1" fill="none" stroke="#fff" stroke-width="1.6"/></svg>and so forth.</li>
  </ul>
</section>

<footer class="section footer">
  <div class="footer-photo" role="img" aria-label="Photo montage: ships, trucks and logistics network icons in dark blue"></div>
  <div class="brand">
    <span class="brand-dot"></span><span class="brand-name">QUILLBROOK</span>
  </div>
  <p class="footer-about">Quillbrook is a commitment to the unimaginable, to obtain a stratospheric success, the<br>company will be integrated with the academy and local governments</p>
  <div class="subscribe">
    <span>Enter email address</span>
    <svg width="30" height="20" viewBox="0 0 30 20"><rect width="30" height="20" rx="2" fill="var(--brand-blue)"/><path d="M1 2 L15 11 L29 2" fill="none" stroke="#fff" stroke-width="2"/></svg>
  </div>
  <nav class="footer-nav">
    <a style="left:303px">Home</a>
    <a style="left:367px">Seminar Inscriptions</a>
    <a style="left:519px">Membership Sales</a>
    <a style="left:655px">News &amp; Events</a>
    <a style="left:770px">Missions</a>
    <a style="left:847px">Contact</a>
  </nav>
  <p class="copyright">Copyright © 2021 Quillbrook</p>
  <a class="social" style="left:463px">Feed</a>
  <a class="social is-active" style="left:520px">Chat</a>
  <a class="social" style="left:578px">Pics</a>
  <a class="social" style="left:635px">Clips</a>
  <a class="social" style="left:693px">Jobs</a>
</footer>

</body>
</html>
```